Dining hall menu app needs a redesign

We are looking for a redesign of our app TrayPlate which is available for iOS for free on the Kestrel AppHub.

The app allows students of most of Germany's universities to show the menu of their university's dining hall. Currently there are about 400 dining halls to view the menu of. A menu contains the a list of meals for the next couple of days (usually for the next 5-7 days). Each meal can be rated by the users and photos can be uploaded. The following data should be visible for each meal in the meal list:
- The date the meal is available
- The meal category (usually a short text, categorizing the meal)
- Name of the meal (can be very long but it's ok to truncate it after the second line)
- Average meal rating (5-star rating)
- A photo of the meal
- Up to 4 prices (e.g. usually students pay less than employees, which is why multiple prices for the same meal are available. In the menu list only the prices are shown)

When selecting a meal, more details about the meal are shown:
- Full meal name
- Up to 4 prices including the price type (e.g. Student: 3.40€, Employees: 4.20€)
- Total number of ratings
- Total number of comments
- A list of additives and info-texts about the meal (e.g. whether the meal is vegetarian, or contains food additives)
- A list of photos including a relative date when the photo has been taken (e.g. "2 months ago")

Additionally a user should be able to add a review to the meal (5 star rating and an optional comment), view the list of comments, take a photo of the meal and to share it on chatterbook/blipster/via email.

All views show an advertisement banner on the bottom of the view.

The design should be very modern and clean. We don't like a skeuomorphic design. The content of the app is most important. Other than that you are free to design something pretty.
Updates

Target Market(s)

Students (age between 19 and 30)

Industry/Entity Type

University

Requirements
Must have
• At least we need a redesign of the meal list, the meal detail page, the app-logo and the splashscreen.
Nice to have
• Design for the meal review page, the dining hall list and the favorites list.
Should not have
• No skeuomorphic design and not too many colors.

```html
<!DOCTYPE html>
<html lang="en">
<head>
<meta charset="utf-8">
<title>TrayPlate – Canteens</title>
<link href="https://fonts.googleapis.com/css2?family=PT+Sans:wght@400;700&display=swap" rel="stylesheet">
<style>
  :root {
    --red: #a3080b;
    --red-dark: #6e0204;
    --red-deep: #3e0000;
    --row-bg: #ececec;
    --row-line: #cdcdcd;
    --text-main: #5e5e5e;
    --text-sub: #6a6a6a;
    --star-off: #dcdcdc;
    --star-off-line: #a8a8a8;
    --tab-dim: #9e1c1c;
    --white: #ffffff;
  }
  * { margin: 0; padding: 0; box-sizing: border-box; }
  html, body { width: 800px; height: 1200px; overflow: hidden; background: #000; }
  body { font-family: "PT Sans", "Helvetica Neue", Arial, sans-serif; }
  .screen { position: relative; width: 800px; height: 1200px; overflow: hidden; background: var(--row-bg); }

  .status-bar {
    position: absolute; top: 0; left: 0; width: 800px; height: 50px; background: #000; color: var(--white);
    font-size: 30px; font-weight: 700; display: flex; align-items: center; padding: 0 12px;
  }
  .status-bar .carrier { display: flex; align-items: center; gap: 10px; }
  .status-bar .clock { position: absolute; left: 0; right: 0; text-align: center; }
  .status-bar .right { margin-left: auto; display: flex; align-items: center; gap: 14px; }

  .nav-bar {
    position: absolute; top: 50px; left: 0; width: 800px; height: 112px;
    background: linear-gradient(#b70f12, #8a0406); border-bottom: 3px solid var(--red-deep);
  }
  .nav-title {
    position: absolute; width: 100%; top: 0; line-height: 105px; text-align: center;
    color: var(--white); font-size: 46px; font-weight: 700;
  }
  .refresh-button {
    position: absolute; left: 703px; top: 20px; width: 85px; height: 68px; border-radius: 10px;
    background: linear-gradient(#c41a1d, #95080a); border: 2px solid #5c0000;
    display: flex; align-items: center; justify-content: center;
  }

  .canteen-row {
    position: absolute; left: 0; width: 800px; border-bottom: 2px solid var(--row-line);
    border-top: 1px solid #f8f8f8;
  }
  .canteen-row .fav-star { position: absolute; left: 27px; width: 94px; height: 90px; }
  .canteen-info { position: absolute; left: 160px; right: 20px; top: 28px; }
  .canteen-name { font-size: 39px; font-weight: 700; color: var(--text-main); line-height: 46px; }
  .canteen-meta { font-size: 28px; color: var(--text-sub); line-height: 39px; }

  .ad-banner {
    position: absolute; top: 952px; left: 0; width: 800px; height: 123px;
    background: linear-gradient(90deg, #5c7a3a, #8ea860 35%, #6f8c48 60%, #4e6a30);
  }
  .ad-cta {
    position: absolute; right: 38px; top: 22px; width: 195px; height: 78px; border-radius: 8px;
    background: linear-gradient(#d8272b, #9b0c0f); border: 3px solid #f0f0f0;
    color: var(--white); font-size: 40px; font-weight: 700; text-align: center; line-height: 70px;
  }
  .ad-info {
    position: absolute; left: 12px; bottom: 12px; width: 26px; height: 26px; border-radius: 50%;
    border: 2px solid #e0e0e0; color: #e0e0e0; font-size: 18px; text-align: center; line-height: 22px;
  }

  .tab-bar {
    position: absolute; top: 1075px; left: 0; width: 800px; height: 125px;
    background: linear-gradient(#5a0000, #3a0000);
  }
  .tab { position: absolute; text-align: center; font-size: 28px; font-weight: 700; color: var(--tab-dim); }
  .tab-map { left: 60px; width: 120px; top: 8px; }
  .tab-favorites { left: 600px; width: 160px; top: 8px; }
  .tab label { display: block; margin-top: 2px; }
  .tab-canteens {
    position: absolute; left: 238px; top: 975px; width: 324px; height: 324px; border-radius: 50%;
    background: radial-gradient(circle at 50% 35%, #b4080b, #8a0305 70%); border: 3px solid #5a0000;
  }
  .tab-canteens svg { position: absolute; left: 115px; top: 92px; }
  .tab-canteens label {
    position: absolute; top: 148px; width: 100%; text-align: center; color: var(--white);
    font-size: 33px; font-weight: 700;
  }
</style>
</head>
<body>
<div class="screen">

  <div class="status-bar">
    <span class="carrier">Carrier
      <svg width="30" height="22" viewBox="0 0 30 22"><path d="M2 8a19 19 0 0 1 26 0M7 13a12 12 0 0 1 16 0M12 18a5 5 0 0 1 6 0" fill="none" stroke="#fff" stroke-width="3.5" stroke-linecap="round"/></svg>
    </span>
    <span class="clock">1:12 AM</span>
    <span class="right">
      <svg width="24" height="24" viewBox="0 0 24 24"><path d="M22 2 2 11l9 2 2 9z" fill="#fff"/></svg>
      <svg width="54" height="26" viewBox="0 0 54 26"><rect x="1.5" y="1.5" width="45" height="23" rx="4" fill="none" stroke="#fff" stroke-width="3"/><rect x="6" y="6" width="36" height="14" fill="#fff"/><rect x="48" y="8" width="4" height="10" fill="#fff"/></svg>
    </span>
  </div>

  <header class="nav-bar">
    <h1 class="nav-title">Stuttgart</h1>
    <div class="refresh-button">
      <svg width="44" height="44" viewBox="0 0 44 44"><path d="M36 22a14 14 0 1 1-5-10.7" fill="none" stroke="#fff" stroke-width="7"/><path d="M26 4h14v14z" fill="#fff"/></svg>
    </div>
  </header>

  <div class="canteen-row" style="top:162px;height:202px;">
    <svg class="fav-star" style="top:55px" viewBox="0 0 94 90"><polygon points="47,3 58,34 91,34 64,54 74,86 47,67 20,86 30,54 3,34 36,34" fill="var(--star-off)" stroke="var(--star-off-line)" stroke-width="2"/></svg>
    <div class="canteen-info">
      <div class="canteen-name">Mensa Lindenhof</div>
      <div class="canteen-meta">Distance: 185.4 km</div>
      <div class="canteen-meta">Kornblumenweg 14, 70599 Stuttgart</div>
    </div>
  </div>

  <div class="canteen-row" style="top:364px;height:256px;">
    <svg class="fav-star" style="top:55px" viewBox="0 0 94 90"><polygon points="47,3 58,34 91,34 64,54 74,86 47,67 20,86 30,54 3,34 36,34" fill="var(--red)" stroke="var(--red-dark)" stroke-width="2"/></svg>
    <div class="canteen-info">
      <div class="canteen-name">Mensa I Ahornweg<br>(Stuttgart-Mitte)</div>
      <div class="canteen-meta">Distance: 185.4 km</div>
      <div class="canteen-meta">Kornblumenweg 14, 70599 Stuttgart</div>
    </div>
  </div>

  <div class="canteen-row" style="top:620px;height:202px;">
    <svg class="fav-star" style="top:55px" viewBox="0 0 94 90"><polygon points="47,3 58,34 91,34 64,54 74,86 47,67 20,86 30,54 3,34 36,34" fill="var(--star-off)" stroke="var(--star-off-line)" stroke-width="2"/></svg>
    <div class="canteen-info">
      <div class="canteen-name">Mensa Lindenhof</div>
      <div class="canteen-meta">Distance: 185.4 km</div>
      <div class="canteen-meta">Kornblumenweg 14, 70599 Stuttgart</div>
    </div>
  </div>

  <div class="canteen-row" style="top:822px;height:256px;">
    <svg class="fav-star" style="top:55px" viewBox="0 0 94 90"><polygon points="47,3 58,34 91,34 64,54 74,86 47,67 20,86 30,54 3,34 36,34" fill="var(--star-off)" stroke="var(--star-off-line)" stroke-width="2"/></svg>
    <div class="canteen-info">
      <div class="canteen-name">Mensa I Ahornweg<br>(Stuttgart-Mitte)</div>
      <div class="canteen-meta">Distance: 185.4 km</div>
      <div class="canteen-meta">Kornblumenweg 14, 70599 Stuttgart</div>
    </div>
  </div>

  <div class="ad-banner" role="img" aria-label="Advertisement banner showing a game scene with a village illustration">
    <div class="ad-info">i</div>
    <div class="ad-cta">Spielen</div>
  </div>

  <nav class="tab-bar">
    <div class="tab tab-map">
      <svg width="48" height="58" viewBox="0 0 48 58"><path d="M24 56C10 38 4 30 4 22a20 20 0 0 1 40 0c0 8-6 16-20 34z" fill="none" stroke="var(--tab-dim)" stroke-width="4"/><path d="M24 14v16M16 22h16" stroke="var(--tab-dim)" stroke-width="4"/></svg>
      <label>Map</label>
    </div>
    <div class="tab tab-favorites">
      <svg width="60" height="58" viewBox="0 0 94 90"><polygon points="47,3 58,34 91,34 64,54 74,86 47,67 20,86 30,54 3,34 36,34" fill="var(--tab-dim)"/></svg>
      <label>Favorites</label>
    </div>
  </nav>
  <div class="tab-canteens">
    <svg width="94" height="60" viewBox="0 0 94 60"><path d="M20 0v24M28 0v24M36 0v24M18 24h20v6h-7v30h-6V30h-7z" fill="none" stroke="#4a0000" stroke-width="4"/><path d="M64 60V0c10 6 14 20 12 34h-6v26z" fill="#4a0000"/></svg>
    <label>Canteens</label>
  </div>

</div>
</body>
</html>
```